Flyer Design Project

We want to design a flyer for a laundromat in San Francisco. It will be used to market the services of the laundromat. I am uploading a .jpg file with details to be highlighted. The flyer should be of size 8.5 in x 11 in and should be attractive and hard hitting. The attachment should only be used for the copy, not for design.

Target Market(s)

Laundromat and laundry users

Requirements
Must have
• Must have a attention grabbing headline
Nice to have
• Pictures

```html
<!DOCTYPE html>
<html lang="en">
<head>
<meta charset="utf-8">
<title>Harlow Laundromat Flyer</title>
<link rel="stylesheet" href="https://fonts.googleapis.com/css2?family=Arimo:wght@400;700&display=swap">
<style>
  :root {
    --tag-red: #d2141a;
    --tag-red-dark: #a50d12;
    --string-gold: #c9a24a;
    --ink: #111111;
    --brand-green: #8cc63f;
    --paper: #ffffff;
    --photo-dark: #3f4a3c;
    --photo-yellow: #f1de8a;
    --photo-skin: #d9a57c;
    --photo-orange: #f08a4b;
    --photo-lime: #c8e07a;
    --photo-steel: #d6dadb;
  }
  html, body {
    margin: 0;
    padding: 0;
    width: 927px;
    height: 1200px;
    overflow: hidden;
    background: var(--paper);
  }
  .flyer {
    position: relative;
    width: 927px;
    height: 1200px;
    overflow: hidden;
    background: var(--paper);
    font-family: "Arimo", Arial, sans-serif;
    color: var(--ink);
  }
  .hero-photo {
    position: absolute;
    left: 0;
    top: 0;
    width: 927px;
    height: 560px;
    background:
      linear-gradient(180deg, rgba(255,255,255,0) 62%, var(--paper) 96%),
      radial-gradient(ellipse 150px 90px at 560px 420px, var(--photo-orange) 0%, rgba(240,138,75,0) 100%),
      radial-gradient(ellipse 150px 100px at 670px 400px, var(--photo-lime) 0%, rgba(200,224,122,0) 100%),
      radial-gradient(ellipse 120px 150px at 200px 200px, var(--photo-skin) 0%, rgba(217,165,124,0) 100%),
      radial-gradient(ellipse 110px 140px at 360px 150px, #c89877 0%, rgba(200,152,119,0) 100%),
      radial-gradient(ellipse 170px 230px at 150px 440px, var(--photo-yellow) 0%, rgba(241,222,138,0) 100%),
      radial-gradient(ellipse 150px 190px at 420px 330px, #8fa3a8 0%, rgba(143,163,168,0) 100%),
      radial-gradient(ellipse 320px 280px at 760px 180px, #f4f4f2 0%, rgba(244,244,242,0) 100%),
      linear-gradient(100deg, var(--photo-dark) 0%, #7b6a4c 22%, #c9b58e 40%, var(--photo-steel) 62%, #eceeec 100%);
  }
  .strings {
    position: absolute;
    left: 0;
    top: 0;
    width: 927px;
    height: 1200px;
  }
  .tag { position: absolute; }
  .tag svg {
    position: absolute;
    inset: 0;
    width: 100%;
    height: 100%;
    overflow: visible;
  }
  .tag-copy {
    position: absolute;
    top: 0;
    bottom: 0;
    display: flex;
    align-items: center;
    justify-content: center;
    text-align: center;
    color: var(--paper);
    font-weight: 700;
    font-size: 27px;
    line-height: 1.13;
    text-shadow: 1px 1px 2px rgba(0,0,0,0.45);
  }
  .tag-clean { left: 118px; top: 492px; width: 310px; height: 208px; transform: rotate(-3deg); }
  .tag-clean .tag-copy { left: 70px; right: 12px; }
  .tag-machines { left: 522px; top: 498px; width: 326px; height: 202px; transform: rotate(3deg); }
  .tag-machines .tag-copy { left: 12px; right: 80px; }
  .tag-nearby { left: 56px; top: 722px; width: 342px; height: 172px; transform: rotate(3deg); }
  .tag-nearby .tag-copy { left: 10px; right: 82px; }
  .tag-service { left: 484px; top: 722px; width: 374px; height: 186px; transform: rotate(4deg); }
  .tag-service .tag-copy { left: 10px; right: 82px; }

  .offer-card {
    position: absolute;
    left: 616px;
    top: 34px;
    width: 290px;
    height: 332px;
    box-sizing: border-box;
    padding-bottom: 40px;
    background: var(--tag-red);
    box-shadow: 4px 8px 12px rgba(0,0,0,0.4);
    transform: rotate(1.5deg);
    display: flex;
    flex-direction: column;
    align-items: center;
    justify-content: center;
    text-align: center;
    color: var(--paper);
    font-weight: 700;
    text-shadow: 1px 1px 2px rgba(0,0,0,0.4);
  }
  .offer-headline { font-size: 52px; line-height: 1.15; }
  .offer-detail { font-size: 36px; line-height: 1.2; }

  .brand {
    position: absolute;
    left: 250px;
    top: 938px;
    display: flex;
    align-items: center;
    gap: 28px;
  }
  .brand-mark {
    width: 128px;
    height: 128px;
    border-radius: 50%;
    background: #c7cdd0;
  }
  .brand-name {
    font-weight: 400;
    font-size: 50px;
    line-height: 1.0;
    color: var(--brand-green);
  }
  .contact {
    position: absolute;
    left: 0;
    width: 927px;
    text-align: center;
    font-weight: 700;
  }
  .contact-address { top: 1072px; font-size: 27px; }
  .contact-hours { top: 1110px; font-size: 16px; }
  .contact-web { top: 1136px; font-size: 30px; }
</style>
</head>
<body>
<div class="flyer">
  <div class="hero-photo" role="img" aria-label="Photo of a smiling couple holding orange and green laundry in front of a row of front-loading washers"></div>

  <svg class="strings" viewBox="0 0 927 1200" aria-hidden="true">
    <g fill="none" stroke="var(--string-gold)" stroke-width="2">
      <path d="M176 612 C130 600 60 590 0 596"/>
      <path d="M176 612 C120 640 50 650 0 648"/>
      <path d="M812 596 C850 580 890 570 927 552"/>
      <path d="M812 596 C860 610 900 620 927 624"/>
      <path d="M346 808 C380 780 420 770 470 760"/>
      <path d="M346 808 C390 820 430 830 470 830"/>
      <path d="M760 842 C820 830 870 820 927 806"/>
      <path d="M760 842 C820 860 880 870 927 868"/>
    </g>
  </svg>

  <div class="offer-card">
    <div class="offer-headline">50% Off</div>
    <div class="offer-detail">Your First<br>Wash &amp; Fold<br>Order</div>
  </div>

  <div class="tag tag-clean">
    <svg viewBox="0 0 310 208" preserveAspectRatio="none" aria-hidden="true">
      <path d="M60 4 H306 V204 H60 L4 146 V62 Z" fill="var(--tag-red)" stroke="var(--tag-red-dark)" stroke-width="2"/>
      <circle cx="58" cy="104" r="14" fill="#f5f0e0" stroke="var(--string-gold)" stroke-width="4"/>
    </svg>
    <div class="tag-copy">Cleanist<br>Laundromat<br>in the<br>Bay Area with<br>Ample Parking</div>
  </div>

  <div class="tag tag-machines">
    <svg viewBox="0 0 326 202" preserveAspectRatio="none" aria-hidden="true">
      <path d="M4 4 H264 L322 60 V142 L264 198 H4 Z" fill="var(--tag-red)" stroke="var(--tag-red-dark)" stroke-width="2"/>
      <circle cx="276" cy="101" r="14" fill="#f5f0e0" stroke="var(--string-gold)" stroke-width="4"/>
    </svg>
    <div class="tag-copy">Large<br>Commercial<br>Washers<br>&amp; Dryers</div>
  </div>

  <div class="tag tag-nearby">
    <svg viewBox="0 0 342 172" preserveAspectRatio="none" aria-hidden="true">
      <path d="M4 4 H282 L338 52 V120 L282 168 H4 Z" fill="var(--tag-red)" stroke="var(--tag-red-dark)" stroke-width="2"/>
      <circle cx="290" cy="86" r="14" fill="#f5f0e0" stroke="var(--string-gold)" stroke-width="4"/>
    </svg>
    <div class="tag-copy">FreshCart,<br>Bean Harbor<br>Jade Wok &amp;<br>Hero Stop Nearby</div>
  </div>

  <div class="tag tag-service">
    <svg viewBox="0 0 374 186" preserveAspectRatio="none" aria-hidden="true">
      <path d="M4 4 H314 L370 56 V130 L314 182 H4 Z" fill="var(--tag-red)" stroke="var(--tag-red-dark)" stroke-width="2"/>
      <circle cx="316" cy="93" r="14" fill="#f5f0e0" stroke="var(--string-gold)" stroke-width="4"/>
    </svg>
    <div class="tag-copy">We'll Do It<br>For You.<br>Wash &amp; Fold<br>Within 24 Hours</div>
  </div>

  <div class="brand">
    <div class="brand-mark" aria-hidden="true"></div>
    <div class="brand-name">harlow<br>laundromat</div>
  </div>

  <div class="contact contact-address">2150 B Harlow St • San Franscisco, CA 94115</div>
  <div class="contact contact-hours">(Next to FreshCart)&nbsp; Open Everyday from 6AM to 10PM</div>
  <div class="contact contact-web">415.555.0182 • www.harlowlaundromat.com</div>
</div>
</body>
</html>
```